Laundry pickup and delivery flyer "Fold Harbor laundry"

I need a flyer "8.5"x11" that tells customers about our pickup and delivery laundry service. our website address is: www.foldharborlaundry.example The flyer should be front and back.

Font styles to use
Sans Serif

Colors
0094D4
00A9DD
6FCCEA
C7EBF8
E9F6FB

```html
<!DOCTYPE html>
<html lang="en">
<head>
<meta charset="utf-8">
<title>Fold Harbor Laundry – Pickup and Delivery Flyer</title>
<link rel="stylesheet" href="https://fonts.googleapis.com/css2?family=Fredoka:wght@500;600&family=Nunito:wght@600;700&display=swap">
<style>
  :root {
    --blue-deep: #0b6db3;
    --blue: #0094D4;
    --blue-bright: #00A9DD;
    --blue-soft: #6FCCEA;
    --blue-pale: #C7EBF8;
    --blue-mist: #E9F6FB;
    --ink: #2a2f36;
    --paper: #ffffff;
    --backdrop: #dcdfe2;
  }
  * { box-sizing: border-box; margin: 0; padding: 0; }
  html, body { width: 1200px; height: 900px; overflow: hidden; }
  body { background: var(--backdrop); font-family: "Nunito", sans-serif; }

  .flyer {
    position: absolute; left: 280px; top: 36px;
    width: 640px; height: 828px;
    background: linear-gradient(180deg, #f4f5f6 0%, var(--paper) 40%);
    overflow: hidden;
  }
  .heading-font { font-family: "Fredoka", sans-serif; }

  .brand { position: absolute; left: 40px; top: 70px; color: var(--blue); }
  .brand-name { font-family: "Fredoka", sans-serif; font-weight: 600; font-size: 40px; line-height: 1; }
  .brand-tag { font-family: "Fredoka", sans-serif; font-weight: 600; font-size: 13px; letter-spacing: 1px; margin-top: 4px; }

  .machine-photo {
    position: absolute; left: 320px; top: 26px; width: 270px; height: 300px;
    background: linear-gradient(160deg, #fafafa 0%, #d9dbdd 60%, #b9bcbf 100%);
    border-radius: 6px;
  }
  .water-splash {
    position: absolute; left: 0; top: 250px; width: 640px; height: 230px;
    background: radial-gradient(ellipse at 30% 40%, var(--blue-bright) 0%, var(--blue-soft) 35%, var(--blue-pale) 60%, rgba(233,246,251,0) 78%),
                linear-gradient(180deg, rgba(255,255,255,0) 40%, var(--blue-pale) 70%, rgba(255,255,255,0) 100%);
  }

  .seal {
    position: absolute; left: 40px; top: 430px; width: 200px; height: 200px;
    border: 10px solid var(--blue); border-radius: 50%; background: var(--paper);
    display: flex; flex-direction: column; align-items: center; justify-content: center; text-align: center;
  }
  .seal-name { font-family: "Fredoka", sans-serif; font-weight: 600; font-size: 34px; line-height: 1.02; color: var(--blue); }
  .seal-tag { font-size: 9px; font-weight: 700; color: var(--blue); margin-top: 6px; letter-spacing: .5px; }

  .headline { position: absolute; left: 318px; top: 470px; font-family: "Fredoka", sans-serif; font-weight: 600; line-height: 1.05; }
  .headline-main { font-size: 37px; color: var(--blue-deep); }
  .headline-accent { font-size: 37px; color: var(--blue-bright); }
  .headline-sub { font-size: 23px; color: var(--blue); margin-top: 2px; }

  .call-bar {
    position: absolute; left: 310px; top: 598px; width: 300px; height: 46px;
    background: var(--blue); border-radius: 23px 0 0 23px;
    color: var(--paper); font-family: "Fredoka", sans-serif; font-weight: 500; font-size: 25px;
    display: flex; align-items: center; justify-content: center;
  }
  .phone { position: absolute; left: 316px; top: 650px; font-family: "Fredoka", sans-serif; font-weight: 600; font-size: 42px; color: var(--blue-deep); letter-spacing: 1px; }
  .website { position: absolute; left: 330px; top: 716px; font-size: 12px; font-weight: 700; letter-spacing: 4px; color: var(--ink); }

  .why-tab {
    position: absolute; left: 0; top: 650px; width: 270px; height: 36px;
    background: var(--blue); border-radius: 0 18px 18px 0;
    color: var(--paper); font-family: "Fredoka", sans-serif; font-weight: 500; font-size: 20px;
    display: flex; align-items: center; padding-left: 28px;
  }
  .why-list { position: absolute; left: 28px; top: 698px; width: 250px; list-style: none; }
  .why-list li { position: relative; padding-left: 22px; font-size: 11px; line-height: 1.35; color: var(--ink); margin-bottom: 6px; }
  .why-list li::before { content: ""; position: absolute; left: 2px; top: 3px; width: 9px; height: 9px; border-radius: 50%; background: var(--blue); }

  .bottom-band { position: absolute; left: 0; bottom: 0; width: 640px; height: 22px; background: var(--blue); }
</style>
</head>
<body>
  <article class="flyer">
    <header class="brand">
      <div class="brand-name">FOLD HARBOR</div>
      <div class="brand-tag">LAUNDRY AND DRY CLEANING</div>
    </header>

    <div class="machine-photo" role="img" aria-label="Photo of a white front-loading washing machine"></div>
    <div class="water-splash" role="img" aria-label="Splash of clear blue water sweeping across the flyer"></div>

    <div class="seal">
      <div class="seal-name">FOLD<br>HARBOR</div>
      <div class="seal-tag">PREMIER LAUNDRY SERVICE</div>
    </div>

    <h1 class="headline">
      <div class="headline-main">LAUNDRY &amp;</div>
      <div class="headline-accent">DRY CLEANING</div>
      <div class="headline-sub">PICKUP AND DELIVERY</div>
    </h1>

    <div class="call-bar">CALL US TODAY</div>
    <div class="phone">555-014-0199</div>
    <div class="website">www.foldharborlaundry.example</div>

    <h2 class="why-tab">WHY FOLD HARBOR?</h2>
    <ul class="why-list">
      <li>Our laundry professionals separate lights and darks to keep your clothes looking great!</li>
      <li>Your items will never be washed with anyone else's</li>
      <li>We use high quality detergents and eco friendly chemicals. No more laundry day!</li>
    </ul>

    <div class="bottom-band"></div>
  </article>
</body>
</html>
```